Business Card Design

We would like a business card that utilizes our current logo and keeps with the same feel - elegant and organic. Our farm isn't about mass production, it's about excellence, education, beautiful events and flowers - people, culture, and community.

Target Market(s)

Patrons to our farm who are interested in weddings, events, or our flowers and vegetables.

Contact Information for Business Card

Name, address, cell email (Rosalind Hepworth, 2718 Wintervale Rd, Fernridge, WA 80517, cell 30.412.6387, email rosalind@wintervalefarm.example)

```html
<!DOCTYPE html>
<html lang="en">
<head>
<meta charset="utf-8">
<title>Wintervale Farm – Business Card</title>
<link rel="stylesheet" href="https://fonts.googleapis.com/css2?family=Marcellus&family=Arimo:wght@400&display=swap">
<style>
  :root {
    --page-bg: #ecebe7;
    --card-white: #fbfbfa;
    --sage: #6f917c;
    --sage-deep: #55705f;
    --gold: #a98a5a;
    --back-light: #86a592;
    --back-dark: #4b6554;
    --white: #ffffff;
  }
  * { margin: 0; padding: 0; box-sizing: border-box; }
  html, body { width: 1200px; height: 960px; overflow: hidden; }
  body { background: var(--page-bg); position: relative; font-family: "Arimo", Arial, sans-serif; }

  .card {
    position: absolute;
    top: 331px;
    width: 520px;
    height: 297px;
    border-radius: 3px;
    box-shadow: 0 6px 18px rgba(0,0,0,0.12);
    overflow: hidden;
  }

  /* Front */
  .card-front { left: 60px; background: var(--card-white); }
  .front-logo {
    position: absolute; left: 118px; top: 30px;
    display: flex; align-items: center; gap: 10px;
    font-family: "Marcellus", serif; font-size: 30px; color: var(--sage);
    letter-spacing: 0.5px;
  }
  .logo-dot { width: 10px; height: 10px; border-radius: 50%; background: var(--gold); }
  .holder-name {
    position: absolute; left: 34px; top: 104px;
    font-family: "Marcellus", serif; font-size: 24px; color: var(--sage-deep);
    letter-spacing: 0.5px;
  }
  .leaf-sprig {
    position: absolute; left: 0; top: 168px; width: 150px; height: 129px;
    background: linear-gradient(135deg, rgba(111,145,124,0.85), rgba(111,145,124,0.35));
    border-top-right-radius: 100% 90%;
  }
  .contact {
    position: absolute; right: 30px; bottom: 26px;
    text-align: right; color: var(--sage-deep); font-size: 14.5px; line-height: 1.3;
  }
  .contact .address { margin-bottom: 10px; }
  .contact-line { display: flex; justify-content: flex-end; align-items: center; gap: 8px; }
  .contact-line .phone { font-size: 17px; }
  .contact-line svg { width: 14px; height: 14px; flex: none; }

  /* Back */
  .card-back {
    left: 620px;
    background: radial-gradient(ellipse at 30% 25%, var(--back-light), var(--back-dark) 85%);
  }
  .back-pattern { position: absolute; inset: 0; }
  .back-logo {
    position: absolute; inset: 0;
    display: flex; align-items: center; justify-content: center; gap: 12px;
    font-family: "Marcellus", serif; font-size: 36px; color: var(--white);
    letter-spacing: 0.5px;
  }
  .back-logo .logo-dot { background: var(--white); width: 12px; height: 12px; }
</style>
</head>
<body>
  <section class="card card-front">
    <div class="front-logo"><span>Wintervale Farm</span><span class="logo-dot"></span></div>
    <div class="holder-name">Rosalind Hepworth</div>
    <div class="leaf-sprig" role="img" aria-label="Illustrated sage-green leafy sprig in the lower left corner"></div>
    <div class="contact">
      <div class="address">2718 Wintervale Rd<br>Fernridge, WA 80517</div>
      <div class="contact-line">
        <span class="phone">30.412.6387</span>
        <svg viewBox="0 0 14 14" aria-hidden="true"><rect x="3.5" y="0.8" width="7" height="12.4" rx="1.3" fill="none" stroke="var(--gold)" stroke-width="1.2"/><line x1="6" y1="11" x2="8" y2="11" stroke="var(--gold)" stroke-width="1.2"/></svg>
      </div>
      <div class="contact-line">
        <span>rosalind@wintervalefarm.example</span>
        <svg viewBox="0 0 14 14" aria-hidden="true"><rect x="0.8" y="3" width="12.4" height="8.4" fill="var(--gold)"/><polyline points="0.8,3 7,8 13.2,3" fill="none" stroke="var(--card-white)" stroke-width="1"/></svg>
      </div>
    </div>
  </section>

  <section class="card card-back">
    <div class="back-pattern" role="img" aria-label="Faint repeating leaf pattern across the green background"></div>
    <div class="back-logo"><span>Wintervale Farm</span><span class="logo-dot"></span></div>
  </section>
</body>
</html>
```